Cafeteria management company.. needs fun, healthy, school lunch menu design!

We need a menu design for cafeteria management company.
We manage several cafeterias and need to convey "healthy", "fun", and entice parents and kids to buy from our daily lunch menu.
We are a local company and have great goodwill/name for service.

go to www.brantleymeals.example to see what our company offers...

This menu will be posted online thru all our schools so we want it to look professional as well.
Currently we use it to communicate lots of pertinent information parents and patrons.
We would like to see designs that include all the attached information, and allows content to be editable going forward..(we change meals throughout the year).

Target Market(s)

Parents of school aged kids. Kids ages 5-18,
Employees of business..

Industry/Entity Type

School

Requirements
Must have
• Looking for a usable template with most areas editable...used for high school and elementary menus
Needs to be easily read and use a font that photocopies well and is popular/accessible by all computers..
There is alot of information to include.
Needs to be 1 page 8.5 x 11.
Can be portrait or landscape
Needs to use the mealbuddo jpeg.
Like the use of color, but will always be printed in black and white or photocopied as such.

```html
<!DOCTYPE html>
<html lang="en">
<head>
<meta charset="utf-8">
<title>Healthy Choice Menu: Elementary School</title>
<link rel="stylesheet" href="https://fonts.googleapis.com/css2?family=Arimo:ital,wght@0,400;0,700;1,400;1,700&family=Open+Sans:wght@300&display=swap">
<style>
:root{
  --ink:#111;
  --red:#e03c2c;
  --peach:#f6d2c3;
  --peach-soft:#f9ddd1;
  --green:#58a83b;
  --link:#1f5fbf;
  --sun:#f6e21c;
  --paper:#fff;
}
*{box-sizing:border-box;margin:0;padding:0}
html,body{width:1200px;height:927px;overflow:hidden;background:var(--paper)}
body{position:relative;font-family:"Arimo",Arial,sans-serif;color:var(--ink)}
.abs{position:absolute}

.title{left:84px;top:28px;font-size:39px;white-space:nowrap}
.title b{font-weight:700;font-style:italic}
.title .level{font-family:"Open Sans",Arial,sans-serif;font-weight:300;font-size:43px}

/* menu grid */
.menu{left:22px;top:82px;width:846px;display:grid;grid-template-columns:40px repeat(5,1fr);
  grid-template-rows:82px 25px 113px 115px 112px 115px 25px 110px}
.day-head{background:var(--peach);padding:8px 0 0 11px;border-left:2px solid var(--ink)}
.day-head:nth-child(2){border-left:none}
.day-head.last{border-top-right-radius:26px}
.day-name{color:var(--red);font-size:21px;line-height:1}
.kettle{font-size:10.5px;font-weight:700;font-style:italic;margin-top:9px;padding-left:6px}
.soup{font-size:9.5px;margin-top:4px;padding-left:6px}
.corner{background:var(--peach);border-top-left-radius:26px}
.row-label{color:var(--red);font-weight:700;font-style:italic;font-size:18px;grid-column:1 / 3;
  padding:3px 0 0 36px;white-space:nowrap;border-bottom:1px solid var(--red)}
.row-gap{border-left:2px solid var(--ink);border-bottom:1px solid var(--red)}
.week-tab{border:1px solid var(--red);border-right:none;border-radius:8px 0 0 8px;position:relative;margin:2px 0}
.week-tab span{position:absolute;left:50%;top:50%;transform:translate(-50%,-50%) rotate(-90deg);
  color:var(--red);font-size:21px;white-space:nowrap}
.shade{background:var(--peach)}
.cell{position:relative;border-left:2px solid var(--ink);display:flex;flex-direction:column;
  text-align:center;font-size:13.3px;line-height:1.16;padding:5px 6px 0}
.cell .meal{flex:1}
.cell .dates{font-size:11.5px;text-align:left;border-top:1px dashed #777;padding:4px 0 3px 6px;margin:0 -6px;white-space:nowrap;overflow:hidden}
.cell.first{border-left:1px solid var(--red)}
.tick{position:absolute;right:6px;bottom:23px;width:17px;height:17px}
.sun{position:absolute;right:6px;bottom:24px;width:16px;height:16px;border-radius:50%;background:var(--sun);border:1px solid #333}
.sun.pair{right:26px}
.optional{padding-top:14px}

/* legend & notes */
.legend{left:55px;top:796px;display:flex;gap:16px;font-size:8.6px;line-height:1.1}
.legend div{display:flex;align-items:flex-start;gap:5px}
.legend .dot{width:12px;height:12px;border-radius:50%;background:var(--sun);border:1px solid #333;flex:none}
.legend .star{font-size:16px;line-height:.8;font-weight:700}
.legend .ring{width:11px;height:11px;border:1.5px solid var(--red);border-radius:50%;flex:none}
.notes{left:20px;top:827px;width:850px;font-size:10.6px;line-height:1.2}
.notes h3{font-size:12.5px;font-style:italic;font-weight:700;margin-left:42px;margin-bottom:2px}

/* sidebar */
.brand{left:940px;top:36px;width:200px;text-align:center}
.brand .mark{width:64px;height:64px;border-radius:50%;background:var(--red);margin:0 auto 20px}
.brand .name{color:var(--red);font-weight:700;font-size:22px}
.brand .tag{color:var(--red);font-size:13px;margin-top:2px}
.brand .year{color:var(--red);font-size:16px;margin-top:5px}
.buddies{left:933px;top:229px;width:218px;height:36px;border-radius:18px;background:linear-gradient(90deg,#cfe8c2,#a9d68f,#cfe8c2)}
.promo{left:890px;top:266px;width:310px;text-align:center}
.promo h2{font-size:22px;font-style:italic;font-weight:700}
.promo .go{font-size:14px;font-weight:700}
.badges{left:940px;top:322px;display:flex;gap:8px}
.badges i{display:block;width:32px;height:24px;border-radius:5px}
.perks{left:893px;top:356px;width:300px;list-style:none;font-size:11.5px;line-height:1.25}
.perks li{position:relative;padding-left:20px;margin-bottom:11px}
.perks svg{position:absolute;left:2px;top:2px}
.win{left:890px;top:492px;width:310px;text-align:center}
.win h2{font-size:19px;font-style:italic;font-weight:700}
.win .sign{font-size:16px;margin-top:1px}
.win p{font-size:12.4px;line-height:1.25;margin-top:6px}
.follow{left:935px;top:597px;font-size:9.5px;font-style:italic;font-weight:700;line-height:1.05;display:flex;align-items:center;gap:10px}
.follow .net{font-style:normal;font-size:17px;color:#3aa6df}
.plan{left:892px;top:638px;width:305px;font-size:12.8px;line-height:1.25}
.plan h2{font-size:16.5px;font-style:italic;font-weight:700}
.plan .url{color:var(--link);font-weight:700;font-style:italic;font-size:14px;text-decoration:underline}
.plan p{margin-top:2px}
.plan .deal{font-weight:700;margin-top:10px}
</style>
</head>
<body>

<h1 class="abs title"><b>Healthy Choice Menu:</b> <span class="level">Elementary School</span></h1>

<div class="abs menu">
  <div class="corner"></div>
  <div class="day-head"><div class="day-name">MONDAY</div><div class="kettle">From the Kettle</div><div class="soup">Chicken Veggie Noodle</div></div>
  <div class="day-head"><div class="day-name">TUESDAY</div><div class="kettle">From the Kettle</div><div class="soup">Tomato Vegetable</div></div>
  <div class="day-head"><div class="day-name">WEDNESDAY</div><div class="kettle">From the Kettle</div><div class="soup">Chicken Rice</div></div>
  <div class="day-head"><div class="day-name">THURSDAY</div><div class="kettle">From the Kettle</div><div class="soup">Corn Chowder</div></div>
  <div class="day-head last"><div class="day-name">FRIDAY</div><div class="kettle">From the Kettle</div><div class="soup">Beef Vegetable</div></div>

  <div class="row-label">Healthy Choice</div>
  <div class="row-gap"></div><div class="row-gap"></div><div class="row-gap"></div><div class="row-gap"></div>

  <!-- week 1 -->
  <div class="week-tab"><span>Week 1</span></div>
  <div class="cell first"><div class="meal">Pineapple Chicken, Veggie Brown Rice, Stir-Fried Veggies, Milk, Sm Oatmeal Cookie</div><svg class="tick" viewBox="0 0 17 17"><rect x="1" y="4" width="12" height="12" fill="none" stroke="#111"/><path d="M3 9l3 4 9-12" fill="none" stroke="#111" stroke-width="1.6"/></svg><div class="dates">Sept. 1-4, Oct. 5-9,</div></div>
  <div class="cell"><div class="meal">Whole Wheat Spaghetti, Lean Meat or Tomato Sauce, Garlic Roll, Milk, Orange Wedges</div><i class="sun"></i><div class="dates">Nov. 2-6, Nov. 30-Dec. 4,</div></div>
  <div class="cell"><div class="meal">2 Pancakes, <small>1/2</small> Sliced Ham, Cucumber Slices, Milk, Chocolate Pudding</div><div class="dates">Jan. 4-7, Feb. 1-5,</div></div>
  <div class="cell"><div class="meal">Mexican Taco Bake, Tossed Garden Salad, Milk, Low-fat Yogurt</div><i class="sun"></i><div class="dates">Mar. 1-5, April 26-30,</div></div>
  <div class="cell"><div class="meal">Creamy Chicken Pasta, Tossed Green Salad, Milk, Fresh Fruit Salad</div><i class="sun"></i><div class="dates">May 24-28, ,June 21-25</div></div>

  <!-- week 2 -->
  <div class="week-tab shade"><span>Week 2</span></div>
  <div class="cell first shade"><div class="meal">Homemade Meatloaf, Carrots, Smashed Potatoes, Gravy, Milk, <small>1/2</small> Banana</div><div class="dates">Sept. 1-4, Oct. 12-16,</div></div>
  <div class="cell shade"><div class="meal">Turkey Pepperoni Panzaroti, Garden Salad, Milk, Low-fat Yogurt</div><svg class="tick" viewBox="0 0 17 17"><rect x="1" y="4" width="12" height="12" fill="none" stroke="#111"/><path d="M3 9l3 4 9-12" fill="none" stroke="#111" stroke-width="1.6"/></svg><div class="dates">Nov 9-13, Dec. 7-11,</div></div>
  <div class="cell shade"><div class="meal">Glazed Baked Ham, Smashed Potatoes, Veggies, Milk, Grapes</div><svg class="tick" viewBox="0 0 17 17"><rect x="1" y="4" width="12" height="12" fill="none" stroke="#111"/><path d="M3 9l3 4 9-12" fill="none" stroke="#111" stroke-width="1.6"/></svg><div class="dates">Jan. 11-14, Feb. 8-12,</div></div>
  <div class="cell shade"><div class="meal">Zesty Italian or Veggie Lasagna, Caesar Salad, Milk, Blueberry Oatmeal Muffin</div><svg class="tick" viewBox="0 0 17 17"><rect x="1" y="4" width="12" height="12" fill="none" stroke="#111"/><path d="M3 9l3 4 9-12" fill="none" stroke="#111" stroke-width="1.6"/></svg><div class="dates">Mar. 8-12, April 5-9,</div></div>
  <div class="cell shade"><div class="meal">Roasted Chicken, Smashed Potatoes &amp; Veggies Milk, Orange Wedges</div><svg class="tick" viewBox="0 0 17 17"><rect x="1" y="4" width="12" height="12" fill="none" stroke="#111"/><path d="M3 9l3 4 9-12" fill="none" stroke="#111" stroke-width="1.6"/></svg><div class="dates">May 3-7, May 31- June 4</div></div>

  <!-- week 3 -->
  <div class="week-tab"><span>Week 3</span></div>
  <div class="cell first"><div class="meal">Whole Wheat Spaghetti,Lean Meat or Tomato Sauce, Roll, Milk, Apple Crisp</div><svg class="tick" viewBox="0 0 17 17"><rect x="1" y="4" width="12" height="12" fill="none" stroke="#111"/><path d="M3 9l3 4 9-12" fill="none" stroke="#111" stroke-width="1.6"/></svg><div class="dates">Sept. 1-4, Oct. 19-23,</div></div>
  <div class="cell"><div class="meal">2 Pancakes, <small>1/2</small> Sliced Ham, Cucumber Slices, Milk, Chocolate Pudding</div><div class="dates">Nov. 16-20, Dec. 14-18,</div></div>
  <div class="cell"><div class="meal">Homemade Goulash, Fresh Garden Salad, Milk, Low-fat Yogurt</div><div class="dates">Jan. 18-22, Feb. 15-19,</div></div>
  <div class="cell"><div class="meal">Mexican Chicken Enchiladas &amp; Rice, Milk, Banana Oatmeal Muffin</div><div class="dates">Mar. 15-19, April 12-16,</div></div>
  <div class="cell"><div class="meal">Roasted Chicken, Smashed Potatoes &amp; Veggies, Milk, Orange Wedges</div><i class="sun pair"></i><svg class="tick" viewBox="0 0 17 17"><rect x="1" y="4" width="12" height="12" fill="none" stroke="#111"/><path d="M3 9l3 4 9-12" fill="none" stroke="#111" stroke-width="1.6"/></svg><div class="dates">May 10-14, June 7-11</div></div>

  <!-- week 4 -->
  <div class="week-tab shade"><span>Week 4</span></div>
  <div class="cell first shade"><div class="meal">Homemade Chicken Pot Pie, Milk, Grapes</div><div class="dates">Sept.1-4, Oct. 26-30,</div></div>
  <div class="cell shade"><div class="meal">Zesty Italian or Veggie Lasagna, Caesar Salad, Milk, Blueberry Oatmeal Muffin</div><i class="sun"></i><div class="dates">Nov. 23-27 Dec. 21-25,</div></div>
  <div class="cell shade"><div class="meal">Grilled Chicken Stir-Fry, Steamed Rice, Milk, Apple Sauce</div><div class="dates">Jan. 25-29, Feb. 22-26,</div></div>
  <div class="cell shade"><div class="meal">Traditional Shepherd's Pie, Garden Salad, Milk, Fresh Fruit Salad</div><i class="sun"></i><div class="dates">Mar. 22-26, April 19-23,</div></div>
  <div class="cell shade"><div class="meal">Creamy Chicken Pasta, Tossed Garden Salad, Milk, Fresh Fruit Salad</div><div class="dates">May 17-21, June 14-18</div></div>

  <div class="row-label">Optional Meal</div>
  <div class="row-gap"></div><div class="row-gap"></div><div class="row-gap"></div><div class="row-gap"></div>

  <div></div>
  <div class="cell first optional"><div class="meal">Chopped Chicken Burger, Roasted Potatoes &amp; Veggies, Milk &amp; Dessert</div></div>
  <div class="cell optional"><div class="meal">Cheesy Pizza, Veggies &amp; Dip, Milk &amp; Dessert</div></div>
  <div class="cell optional"><div class="meal">Soft Beef Taco, Mexican Rice, Milk &amp; Dessert</div></div>
  <div class="cell optional"><div class="meal">Pepperoni Pizza, Caesar Salad, Milk &amp; Dessert</div></div>
  <div class="cell optional"><div class="meal">Oven-Baked Chicken Nuggets, Potato Wedges, Milk &amp; Dessert</div></div>
</div>

<div class="abs legend">
  <div><i class="dot"></i>A la carte any smiley-face!</div>
  <div><svg width="14" height="14" viewBox="0 0 17 17"><rect x="1" y="4" width="12" height="12" fill="none" stroke="#111"/><path d="M3 9l3 4 9-12" fill="none" stroke="#111" stroke-width="1.6"/></svg>Ingredients used are sourced within/in<br>100 miles of Atlantic Canada</div>
  <div><span class="star">*</span>Vegetarian meals are always available,<br>please ask the cafeteria manager.</div>
  <div><i class="ring"></i>Gluten- Free meal already</div>
  <div><i class="ring"></i>Gluten- Free meal by request</div>
</div>

<div class="abs notes">
  <h3>Healthy Choice Menu:</h3>
  <p>Variations may occur due to difference in suppliers, ingredient substitutions, recipe revisions, meal assembly at the cafeteria, and/or seasons of the year. Certain menu items may not be available at all locations. We encourage anyone with food allergies, sensitivities or special dietary needs to contact/notify the cafeteria manager. We will work with you the very best we can. Brantley Meal Service Management Inc. and its employees do not assume responsibility for a particular allergy or sensitivity to any foods we provided in an of our cafeterias.</p>
</div>

<div class="abs brand">
  <div class="mark"></div>
  <div class="name">Brantley Meals</div>
  <div class="tag">Healthy Food Service Solutions</div>
  <div class="year">2011/2012</div>
</div>

<div class="abs buddies" role="img" aria-label="Row of cheerful cartoon apple mascots"></div>

<div class="abs promo">
  <h2>Be a Meal Buddo!</h2>
  <div class="go">go to brantleymeals.example</div>
</div>

<div class="abs badges" aria-hidden="true">
  <i style="background:#e8322b"></i><i style="background:#1d3d8f"></i><i style="background:#f2c61f"></i><i style="background:#3a9fd8"></i>
</div>

<ul class="abs perks">
  <li><svg width="12" height="10" viewBox="0 0 12 10"><path d="M1 5l3 4 7-8" fill="none" stroke="#111" stroke-width="1.5"/></svg>Join our e mail list &amp; get GREAT COUPONS on our healthy meals and snacks!</li>
  <li><svg width="12" height="10" viewBox="0 0 12 10"><path d="M1 5l3 4 7-8" fill="none" stroke="#111" stroke-width="1.5"/></svg>Buy your meal plans online &amp; manage your lunch money!</li>
  <li><svg width="12" height="10" viewBox="0 0 12 10"><path d="M1 5l3 4 7-8" fill="none" stroke="#111" stroke-width="1.5"/></svg>All names entered into wicked contests. Great prizes available. 100 % opt-in.</li>
</ul>

<div class="abs win">
  <h2>Win Free Lunch for a Month!</h2>
  <div class="sign">Sign-up Today!</div>
  <p>If you have a great coupon idea or comment,<br>please let us know! E mail us at:<br>mealbuddo@brantleymeals.example</p>
</div>

<div class="abs follow"><span>Follow us and be fed well<br>@mealbuddo on</span><span class="net">Chirpline</span></div>

<div class="abs plan">
  <h2>Healthy Meal Plan: Buy Online at</h2>
  <div><span class="url">www.brantleymeals.example</span> or by cheque.</div>
  <p>The meal plan may be purchased weekly or monthly. Please make cheque payable to: Brantley Meal Service. See the Cafeteria Manager for details on meal plan purchase. Unused tickets/meals are valid until the end of the current school year. Non-consecutive days are allowed.</p>
  <p class="deal">Purchase 5 or more meals and receive<br>a 20 % discount per meal, <span style="font-weight:400">when the plan is purchased weekly/monthy. Menu dates as per meal served, are subject to change. Please contact cafeteria manger for meal/date confirmation.</span></p>
</div>

</body>
</html>
```